Business to Business Website Homepage Design

Hi, My Web Developer is giving me designs that aren't quite taking my fancy as far as visual impact. I'd love to see designs come out which are simple, fresh and powerful.
I just want a PDF document that I can give to my web developer to follow, so this project is NOT to make a website, its to design the homepage.
I would like it to scroll down through different areas of my website on the homepage. Our colours are Blood Orange, White, Grey & Black.
I like these websites:
Simplicity
https://www.quenzaro.com/au/webapps/mpp/home
Our Team Section
http://bremlitch.com.au/
We'd like our logo on top left. Nav bar top right. Have an image which we can place a headline subject on + video icon which will pop out with a video and opt in for name and email with a heading so people know what they're opting in for.
The next section should have a lot of white space, this "What we do" which is 1) Grow in size so your business can get bigger 2) increase in value, so you maximise what your business is worth 3) Free up your time, so you can live the lifestyle you've always wanted. Our brief was we want image/text combo with a lot of white space,
Then we have our services
After Services, would like to have a "Why Work With Us" section
Then a testimonials section
Then "Our Team"
Then contact us.
Thats pretty much it, we'd just love some different ideas, these guys are almost there, but just need more impact.
Updates
Target Market(s)
Business Owners between $1m to $3m turnover
Industry/Entity Type
Business
Number of Pages Required
1 page
Look and feel
Each slider illustrates characteristics of the customer's brand and the style your logo design should communicate.

```html
<!DOCTYPE html>
<html lang="en">
<head>
<meta charset="utf-8">
<title>Lodestar Partners — Home</title>
<link href="https://fonts.googleapis.com/css2?family=Lato:ital,wght@0,300;0,400;0,700;0,900;1,400;1,700&display=swap" rel="stylesheet">
<style>
:root{
  --red:#e0332b;
  --red-dark:#c42820;
  --ink:#222222;
  --charcoal:#333333;
  --grey:#6b6b6b;
  --light:#f2f2f2;
  --line:#dddddd;
  --white:#ffffff;
  --footer:#262626;
  --footer-deep:#161616;
}
*{box-sizing:border-box;margin:0;padding:0}
html,body{width:1200px;height:3797px;overflow:hidden}
body{font-family:'Lato',Arial,sans-serif;color:var(--ink);background:var(--white);position:relative}
section,header,footer{position:absolute;left:0;width:1200px}
.abs{position:absolute}

/* Hero */
.hero{top:0;height:689px;background:
  radial-gradient(ellipse 420px 260px at 22% 55%,rgba(120,105,95,.55),transparent 70%),
  radial-gradient(ellipse 380px 300px at 80% 35%,rgba(95,85,80,.5),transparent 70%),
  linear-gradient(180deg,#3b3432 0%,#2d2826 55%,#1c1918 100%)}
.brand{left:56px;top:38px;display:flex;align-items:center;gap:12px}
.brand-dot{width:56px;height:56px;border-radius:50%;background:var(--red)}
.brand-name{font-weight:900;font-size:30px;color:var(--white);letter-spacing:1px;text-transform:uppercase;line-height:1}
.nav{left:536px;top:60px;display:flex;align-items:center;gap:28px;font-size:13px;color:var(--white);text-transform:uppercase}
.nav .current{border:2px solid var(--white);border-radius:20px;padding:8px 14px}
.nav .subscribe{background:var(--red);border-radius:24px;padding:13px 34px;margin-left:2px}
.dotted{left:134px;width:934px;border-top:2px dotted rgba(255,255,255,.45)}
.pillars{left:150px;top:228px;width:904px;display:flex;justify-content:space-between;font-weight:300;font-size:36px;color:#e6e6e6;text-transform:uppercase}
.pillars span+span{border-left:1px solid rgba(255,255,255,.4);padding-left:16px}
.motto{left:0;width:1200px;top:318px;text-align:center;font-weight:700;font-style:italic;font-size:19px;line-height:30px;color:var(--white)}
.btn-signup{left:497px;top:418px;width:196px;height:43px;border-radius:22px;background:var(--red);color:var(--white);font-size:14px;font-weight:700;text-align:center;line-height:43px}
.play{left:559px;top:491px}
.notch{left:564px;top:653px;z-index:3}

/* What we do */
.benefits{top:689px;height:400px;background:var(--white)}
.benefit{top:50px;width:300px;text-align:center}
.benefit h3{font-weight:400;font-size:14px;line-height:19px;color:#555;text-transform:uppercase;height:40px}
.benefit .photo{margin:18px auto 0;width:292px;height:165px;border:6px solid #e9e9e9}
.benefit p{margin-top:14px;font-size:12px;line-height:19px;color:#444}
.ph-growth{background:radial-gradient(ellipse at 70% 40%,#3a4f6a 0%,transparent 60%),linear-gradient(120deg,#dfe5ec 0%,#9fb0c4 45%,#24324a 100%)}
.ph-car{background:radial-gradient(ellipse at 55% 60%,#d9b79a 0%,transparent 45%),linear-gradient(135deg,#cfd8e0 0%,#7d8c99 50%,#37424c 100%)}
.ph-board{background:radial-gradient(ellipse at 55% 65%,#e9dcc8 0%,transparent 40%),linear-gradient(135deg,#f1f1f1 0%,#c7c7c7 50%,#8d8d8d 100%)}

/* Services */
.services{top:1089px;height:683px;background:var(--light)}
.section-title{width:1200px;text-align:center;font-weight:400;font-size:38px;color:var(--ink);text-transform:uppercase;letter-spacing:.5px}
.rule{left:400px;width:400px;border-top:1px solid var(--line)}
.rule-dot{left:594px;width:12px;height:12px;border-radius:50%;background:var(--line)}
.service-grid{left:110px;top:115px;width:1020px;display:grid;grid-template-columns:340px 340px 340px}
.service{text-align:center;height:300px}
.service:nth-child(2),.service:nth-child(5){border-left:1px solid var(--line);border-right:1px solid var(--line)}
.service:nth-child(-n+3){border-bottom:1px solid var(--line);height:259px}
.service:nth-child(n+4){padding-top:43px}
.service .icon{width:112px;height:112px;border-radius:50%;background:var(--charcoal);margin:0 auto;border:4px solid #e4e4e4;box-shadow:0 0 0 2px #999 inset;display:flex;align-items:center;justify-content:center}
.service h4{margin-top:30px;font-weight:400;font-size:24px;color:var(--ink);text-transform:uppercase}
.service p{margin-top:6px;font-size:12px;line-height:16px;color:#555}
.service .more{display:block;margin:16px auto 0;width:18px;height:18px;background:var(--ink);color:var(--white);font-size:16px;line-height:17px;font-weight:700}

/* Why work with us */
.why{top:1772px;height:507px;background:var(--white)}
.why-photo{left:69px;top:102px;width:354px;height:354px;border-radius:50%;border:8px solid #f0f0f0;
  background:radial-gradient(circle at 55% 40%,#2d3540 0 9%,transparent 10%),radial-gradient(circle at 30% 60%,#9aa3ad 0 14%,transparent 15%),radial-gradient(circle at 50% 50%,#f7f8fa 0%,#dfe3e8 55%,#a8b0b9 100%)}
.step{display:flex;align-items:center;gap:14px;font-size:14px;color:#333;text-transform:uppercase}
.step b{width:44px;height:44px;border-radius:50%;background:var(--red);color:var(--white);display:flex;align-items:center;justify-content:center;font-size:20px;font-weight:700;border:3px solid #fff;box-shadow:0 0 0 1px #ddd}
.why-copy{left:739px;top:97px;width:360px;font-size:13px;line-height:20px;color:#333}

/* Testimonials */
.testimonials{top:2279px;height:367px;background:
  radial-gradient(ellipse 300px 200px at 65% 30%,rgba(110,130,150,.45),transparent 70%),
  linear-gradient(110deg,#1b2734 0%,#33475a 50%,#141d27 100%)}
.testimonials .section-title{color:var(--white);top:38px}
.arrow{top:2462px;width:44px;height:44px}
.avatar{left:119px;top:139px;width:152px;height:152px;border-radius:50%;background:radial-gradient(circle at 50% 40%,#e6c7b0 0 30%,#6b4a36 31% 45%,#d8dde2 46%,#a5adb5 100%);border:5px solid #fff}
.client{left:291px;top:183px;color:var(--white)}
.client strong{display:block;font-weight:400;font-size:28px}
.client span{font-size:13px;color:#d0d0d0}
.quote{left:514px;top:159px;width:600px;font-style:italic;font-weight:700;font-size:14px;line-height:22px;color:var(--white)}

/* Team */
.team{top:2646px;height:696px;background:var(--white)}
.team-sub{top:72px;width:1200px;text-align:center;font-size:13px;color:#333;text-transform:uppercase}
.filters{top:132px;width:1200px;text-align:center;font-size:12px;color:#555;text-transform:uppercase}
.filters .on{color:var(--red);font-weight:700}
.team-grid{top:190px;left:0;width:1200px;display:grid;grid-template-columns:repeat(4,300px);grid-auto-rows:253px}
.member{position:relative}
.m1{background:radial-gradient(ellipse 90px 140px at 55% 60%,#f1ece6,transparent 70%),linear-gradient(135deg,#a58a6c,#4a3828)}
.m2{background:radial-gradient(ellipse 100px 140px at 50% 60%,#5c5856,transparent 70%),linear-gradient(135deg,#6a6a6a,#2c2c2c)}
.m3{background:radial-gradient(ellipse 90px 140px at 50% 60%,#f6f3ee,transparent 70%),linear-gradient(135deg,#eceef1,#9ea8b3)}
.m4{background:radial-gradient(ellipse 100px 140px at 55% 65%,#2f3947,transparent 70%),linear-gradient(135deg,#b9c3cd,#56606b)}
.m5{background:radial-gradient(ellipse 100px 140px at 50% 65%,#d5d3d0,transparent 70%),linear-gradient(135deg,#8f8a83,#4e4942)}
.m6{background:radial-gradient(ellipse 100px 140px at 50% 65%,#5b6a7c,transparent 70%),linear-gradient(135deg,#c2573f,#5a2f22)}
.m7{background:radial-gradient(ellipse 100px 140px at 50% 65%,#1f2836,transparent 70%),linear-gradient(135deg,#d7cdbd,#7b7064)}
.m8{background:radial-gradient(ellipse 100px 140px at 50% 65%,#1d1d22,transparent 70%),linear-gradient(135deg,#b9a994,#6b5e50)}
.member-card{position:absolute;left:20px;top:20px;right:20px;bottom:20px;border:2px solid rgba(255,255,255,.7);text-align:center;color:var(--white);background:rgba(40,40,40,.45)}
.member-card .social{width:58px;height:58px;border-radius:50%;border:3px solid #fff;margin:100px auto 0}
.member-card strong{display:block;margin-top:14px;font-size:15px;font-weight:700;text-transform:uppercase}
.member-card span{font-size:14px;text-transform:uppercase}

/* Contact */
.contact{top:3342px;height:405px;background:var(--footer);color:var(--white)}
.contact h5{font-weight:700;font-size:20px}
.label{font-size:13px;font-weight:700}
.field{background:#f1f1f1;height:38px;width:236px;border-radius:2px}
.message{left:319px;top:117px;width:197px;height:190px;background:#f1f1f1}
.btn-send{left:423px;top:324px;width:93px;height:33px;background:var(--red);color:var(--white);font-size:14px;font-weight:700;text-align:center;line-height:33px}
.chat{left:492px;top:32px;width:30px;height:30px;border-radius:50%;background:var(--red)}
.small{font-size:12px;line-height:17px;color:#ddd}
.email-box{left:625px;top:142px;width:190px;height:36px;background:#fff;color:#999;font-size:12px;line-height:36px;padding-left:34px}
.go{left:815px;top:142px;width:37px;height:36px;background:var(--red);font-size:13px;font-weight:700;text-align:center;line-height:36px}
.quick{right:76px;text-align:right}
.quick li{list-style:none;font-size:12px;line-height:24px;color:#ddd}
.map{left:942px;top:238px;width:182px;height:107px;background:linear-gradient(135deg,#e8e3d4,#c9d6c0 60%,#b7cfe0)}
.bottom-bar{top:3747px;height:50px;background:var(--footer-deep)}
.bottom-bar p{position:absolute;left:60px;top:18px;font-size:12px;color:#ccc}
.social-row{position:absolute;left:968px;top:9px;display:flex;gap:10px}
.social-row i{width:32px;height:32px;border-radius:50%;background:#d6d6d6}
</style>
</head>
<body>

<header class="hero" role="img" aria-label="Darkened photo of a business meeting behind the headline">
  <div class="abs brand"><span class="brand-dot"></span><span class="brand-name">Lodestar Partners</span></div>
  <nav class="abs nav">
    <span class="current">Home</span><span>Services</span><span>Events</span><span>Jobs</span><span>Contact Us</span><span class="subscribe">Subscribe</span>
  </nav>
  <div class="abs dotted" style="top:212px"></div>
  <div class="abs pillars"><span>Your Business</span><span>Your Success</span><span>Your Life Style</span></div>
  <div class="abs dotted" style="top:291px"></div>
  <p class="abs motto">"We Exist To Help People Create Better Livelihoods So They Can Follow Their Dreams And Live<br>Life To It's Fullest"</p>
  <div class="abs btn-signup">SIGN UP NOW!</div>
  <svg class="abs play" width="82" height="82" viewBox="0 0 82 82"><circle cx="41" cy="41" r="38" fill="none" stroke="#fff" stroke-width="4"/><path d="M33 26 L57 41 L33 56 Z" fill="#fff"/></svg>
</header>

<svg class="abs notch" width="72" height="72" viewBox="0 0 72 72" style="position:absolute"><path d="M36 0 L68 18 L68 54 L36 72 L4 54 L4 18 Z" fill="#e0332b"/><path d="M26 30 L36 40 L46 30" fill="none" stroke="#fff" stroke-width="4"/></svg>

<section class="benefits">
  <div class="abs benefit" style="left:64px"><h3>Grow in size so your business can<br>get bigger</h3><div class="photo ph-growth" role="img" aria-label="Businessman drawing a rising growth chart"></div><p>Lorem ipsum dolor sit amet, consectetuer adipiscing elit, sed diam nonummy nibh euismod tincidunt ut laoreet dolore magna aliquam erat.</p></div>
  <div class="abs benefit" style="left:450px"><h3>Increase in value, so you maximise<br>what your business is worth</h3><div class="photo ph-car" role="img" aria-label="Smiling couple in a new car"></div><p>Lorem ipsum dolor sit amet, consectetuer adipiscing elit, sed diam nonummy nibh euismod tincidunt ut laoreet dolore magna aliquam erat.</p></div>
  <div class="abs benefit" style="left:836px"><h3>Free up your time, so you can live the<br>lifestyle you've always wanted!</h3><div class="photo ph-board" role="img" aria-label="Woman in front of a chalkboard of sketched ideas"></div><p>Lorem ipsum dolor sit amet, consectetuer adipiscing elit, sed diam nonummy nibh euismod tincidunt ut laoreet dolore magna aliquam erat.</p></div>
</section>

<section class="services">
  <h2 class="abs section-title" style="top:20px">Our Services</h2>
  <div class="abs rule" style="top:83px"></div><div class="abs rule-dot" style="top:77px"></div>
  <div class="abs service-grid">
    <div class="service"><div class="icon"><svg width="60" height="60" viewBox="0 0 60 60" fill="#fff"><circle cx="30" cy="18" r="7"/><path d="M19 44 C19 32 41 32 41 44 Z"/><circle cx="15" cy="23" r="5"/><path d="M6 42 C6 33 20 31 22 36 L18 42 Z"/><circle cx="45" cy="23" r="5"/><path d="M54 42 C54 33 40 31 38 36 L42 42 Z"/></svg></div><h4>People</h4><p>Lorem ipsum dolor sit amet, consectetuer<br>adipiscing elit, sed diam nonummy nibh</p><span class="more">+</span></div>
    <div class="service"><div class="icon"><svg width="60" height="60" viewBox="0 0 60 60"><rect x="12" y="12" width="38" height="26" rx="2" fill="none" stroke="#fff" stroke-width="4"/><path d="M27 38 L25 46 L37 46 L35 38" fill="#fff"/><rect x="21" y="46" width="20" height="3" fill="#fff"/><circle cx="12" cy="40" r="7" fill="#fff"/><circle cx="12" cy="40" r="3" fill="#333"/></svg></div><h4>Business Systems</h4><p>Lorem ipsum dolor sit amet, consectetuer<br>adipiscing elit, sed diam nonummy nibh</p><span class="more">+</span></div>
    <div class="service"><div class="icon"><svg width="60" height="60" viewBox="0 0 60 60" fill="#fff"><rect x="14" y="12" width="32" height="8" rx="2"/><rect x="14" y="23" width="32" height="8" rx="2"/><rect x="10" y="34" width="22" height="8" rx="2"/><rect x="10" y="45" width="22" height="8" rx="2"/><circle cx="42" cy="44" r="10"/><text x="42" y="49" font-size="13" font-weight="700" text-anchor="middle" fill="#333" font-family="Lato,Arial,sans-serif">$</text></svg></div><h4>Funding</h4><p>Lorem ipsum dolor sit amet, consectetuer<br>adipiscing elit, sed diam nonummy nibh</p><span class="more">+</span></div>
    <div class="service"><div class="icon"><svg width="60" height="60" viewBox="0 0 60 60" fill="#fff"><rect x="12" y="22" width="36" height="9"/><rect x="15" y="33" width="30" height="17"/><rect x="28" y="22" width="4" height="28" fill="#333"/><path d="M30 21 C22 10 14 16 22 21 Z M30 21 C38 10 46 16 38 21 Z"/></svg></div><h4>New Earning Stream</h4><p>Lorem ipsum dolor sit amet, consectetuer<br>adipiscing elit, sed diam nonummy nibh</p><span class="more">+</span></div>
    <div class="service"><div class="icon"><svg width="60" height="60" viewBox="0 0 60 60"><rect x="10" y="10" width="40" height="40" rx="3" fill="#fff"/><path d="M16 42 L26 30 L33 36 L44 20" fill="none" stroke="#333" stroke-width="4"/><path d="M38 19 L45 18 L45 25" fill="none" stroke="#333" stroke-width="3"/></svg></div><h4>New Markets</h4><p>Lorem ipsum dolor sit amet, consectetuer<br>adipiscing elit, sed diam nonummy nibh</p><span class="more">+</span></div>
    <div class="service"><div class="icon"><svg width="60" height="60" viewBox="0 0 60 60" fill="#fff"><path d="M6 24 L16 16 L24 22 L18 28 Z"/><path d="M54 24 L44 16 L36 22 L42 28 Z"/><path d="M16 26 L28 20 L40 20 L46 30 L34 42 C32 44 30 44 28 42 L16 32 Z"/></svg></div><h4>New Business</h4><p>Lorem ipsum dolor sit amet, consectetuer<br>adipiscing elit, sed diam nonummy nibh</p><span class="more">+</span></div>
  </div>
</section>

<section class="why">
  <h2 class="abs section-title" style="top:18px">Why Work With Us?</h2>
  <div class="abs rule" style="top:80px"></div><div class="abs rule-dot" style="top:74px"></div>
  <div class="abs why-photo" role="img" aria-label="Overhead view of a team working around a table"></div>
  <div class="abs step" style="left:340px;top:103px"><b>1</b>Innovation</div>
  <div class="abs step" style="left:388px;top:163px"><b>2</b>Strategies</div>
  <div class="abs step" style="left:413px;top:244px"><b>3</b>Growth</div>
  <div class="abs step" style="left:391px;top:330px"><b>4</b>Expertise</div>
  <div class="abs step" style="left:340px;top:401px"><b>5</b>Results</div>
  <svg class="abs" style="left:633px;top:127px" width="66" height="294" viewBox="0 0 66 294"><path d="M2 2 C40 2 34 40 34 90 C34 130 40 145 64 147 C40 149 34 164 34 204 C34 254 40 292 2 292" fill="none" stroke="#e3e3e3" stroke-width="10"/></svg>
  <p class="abs why-copy">Lorem ipsum dolor sit amet, consectetuer adipiscing elit, sed diam nonummy nibh euismod tincidunt ut laoreet dolore magna aliquam erat volutpat. Ut wisi enim ad minim veniam, quis nostrud exerci tation ullamcorper suscipit lobortis nisl ut aliquip ex ea commodo consequat. Duis autem vel eum iriure dolor in hendrerit in vulputate velit esse molestie consequat, vel illum dolore eu feugiat nulla facilisis at vero eros et accumsan et iusto odio dignissim qui blandit praesent luptatum zzril delenit augue duis dolore te feugait nulla facilisi.</p>
</section>

<section class="testimonials" role="img" aria-label="Blurred office scene behind client testimonials">
  <h2 class="abs section-title">Client Testimonials</h2>
  <div class="abs avatar" role="img" aria-label="Portrait of the client"></div>
  <div class="abs client"><strong>Nora Vale</strong><span>Director, CEO</span></div>
  <p class="abs quote">Lorem ipsum dolor sit amet, consectetuer adipiscing elit, sed diam nonummy nibh euismod tincidunt ut laoreet dolore magna aliquam erat volutpat. Ut wisi enim ad minim veniam, quis nostrud exerci tation ullamcorper suscipit lobortis nisl ut aliquip ex ea commodo consequat. Duis autem vel eum iriure dolor in hendrerit in vulputate velit esse molestie consequat, vel illum dolore eu feugiat nulla facilisis at vero eros.</p>
</section>
<svg class="abs arrow" style="left:41px;position:absolute" viewBox="0 0 44 44"><circle cx="22" cy="22" r="20" fill="none" stroke="#fff" stroke-width="2"/><path d="M25 14 L17 22 L25 30" fill="none" stroke="#fff" stroke-width="2.5"/></svg>
<svg class="abs arrow" style="left:1128px;position:absolute" viewBox="0 0 44 44"><circle cx="22" cy="22" r="20" fill="none" stroke="#fff" stroke-width="2"/><path d="M19 14 L27 22 L19 30" fill="none" stroke="#fff" stroke-width="2.5"/></svg>

<section class="team">
  <h2 class="abs section-title" style="top:12px">Our Team</h2>
  <p class="abs team-sub">Meet our expert team of efficient employees</p>
  <div class="abs rule" style="top:106px;left:300px;width:600px"></div>
  <p class="abs filters"><span class="on">All</span> &nbsp;|&nbsp; Management &nbsp;|&nbsp; Technical</p>
  <div class="abs team-grid">
    <div class="member m1" role="img" aria-label="Team member photo"></div>
    <div class="member m2" role="img" aria-label="Team member photo with profile overlay"><div class="member-card"><div class="social"></div><strong>Reid Calloway</strong><span>Managing Director</span></div></div>
    <div class="member m3" role="img" aria-label="Team member photo"></div>
    <div class="member m4" role="img" aria-label="Team member photo"></div>
    <div class="member m5" role="img" aria-label="Team member photo"></div>
    <div class="member m6" role="img" aria-label="Team member photo"></div>
    <div class="member m7" role="img" aria-label="Team member photo"></div>
    <div class="member m8" role="img" aria-label="Team member photo"></div>
  </div>
</section>

<section class="contact">
  <h5 class="abs" style="left:60px;top:34px">Want us to get back to you</h5>
  <div class="abs chat"></div>
  <span class="abs label" style="left:60px;top:90px">Your Name</span>
  <div class="abs field" style="left:60px;top:114px"></div>
  <span class="abs label" style="left:60px;top:170px">Phone Number</span>
  <div class="abs field" style="left:60px;top:192px"></div>
  <span class="abs label" style="left:60px;top:245px">Email</span>
  <div class="abs field" style="left:60px;top:266px"></div>
  <span class="abs label" style="left:319px;top:90px">Type your message here</span>
  <div class="abs message"></div>
  <div class="abs btn-send">SEND</div>

  <span class="abs label" style="left:625px;top:38px">Sign up to our Newsletter</span>
  <p class="abs small" style="left:625px;top:64px;width:240px">Phasellus ullamcorper aliquet tortor, nec ornare magna pharetra Pellentesque quis dui quam. Cras ut ullamcorper</p>
  <div class="abs email-box">Email</div>
  <div class="abs go">GO</div>
  <span class="abs label" style="left:651px;top:220px">Our Address</span>
  <svg class="abs" style="left:651px;top:250px" width="14" height="20" viewBox="0 0 14 20"><path d="M7 0 C3 0 0 3 0 7 C0 12 7 20 7 20 C7 20 14 12 14 7 C14 3 11 0 7 0 Z" fill="#ddd"/><circle cx="7" cy="7" r="2.5" fill="#262626"/></svg>
  <p class="abs small" style="left:674px;top:250px;width:200px">52 Harlow Street, Adelaide, SA,<br>5000, Australia</p>
  <svg class="abs" style="left:651px;top:322px" width="14" height="14" viewBox="0 0 14 14"><path d="M3 0 L6 4 L4 6 C5 8 6 9 8 10 L10 8 L14 11 L12 14 C6 14 0 8 0 2 Z" fill="#ddd"/></svg>
  <p class="abs small" style="left:674px;top:320px">Call: +08 8000 4417</p>
  <svg class="abs" style="left:651px;top:368px" width="16" height="12" viewBox="0 0 16 12"><rect width="16" height="12" fill="#ddd"/><path d="M0 0 L8 7 L16 0" fill="none" stroke="#262626" stroke-width="1.5"/></svg>
  <p class="abs small" style="left:674px;top:365px">info@lodestarpartners.com</p>

  <span class="abs label quick" style="top:38px">Quick Link</span>
  <ul class="abs quick" style="top:60px"><li>Home</li><li>Services</li><li>Events</li><li>Jobs</li><li>Contact Us</li></ul>
  <span class="abs label quick" style="top:220px">Our Location Map</span>
  <div class="abs map" role="img" aria-label="Street map showing the office location"></div>
</section>

<footer class="bottom-bar">
  <p>Copyright 2015 Lodestar Partners. All Rights Reserved.</p>
  <div class="social-row"><i></i><i></i><i></i><i></i></div>
</footer>

</body>
</html>
```